Registry Program Flyer design 2 - MX Bridge registry

We need two different flyers that will be distributed via web, email and print. This project is for the second of the two flyers.

The audience is patients and family members of patients with a specific disease. The flyer will be used to make patients aware of our web-based registry programs, and to inform/encourage patients to join.

An example prototype flyer with the text that should be used is attached. We would like to improve the design and layout of the flyer, while retaining as much of the language as appropriate.

The MXBridge flyer should use the logo provided in the example and a color scheme compatible with the logo. The flyer may use the pictures included in the prototype.

If possible, a final format that allows us to edit the text is preferred. If this is not possible, we will finalize the text after receiving a prototype. Changes to the text will likely be minor.

Note: The design of the flyers for this project and the other project (Registry Program Flyer Design 1 - RTQV registry) can be similar in style, however, they should not be duplicates.

Deliverables will be a final .PSD (photoshop) file with layers so we can edit text if necessary.

Target Market(s)

Physicians and healthcare professionals.

Requirements
Must have
• Use the attached logo and colors.

```html
<!DOCTYPE html>
<html lang="en">
<head>
<meta charset="utf-8">
<title>MX Bridge Registry Flyer</title>
<link rel="stylesheet" href="https://fonts.googleapis.com/css2?family=Source+Sans+3:ital,wght@0,400;0,600;0,700;1,400&display=swap">
<style>
  :root {
    --red: #d7212a;
    --ink: #1d1d1b;
    --grey-panel: #d9d9d9;
    --dark-panel: #333333;
    --white: #ffffff;
    --body-grey: #2b2b2b;
    --sky: #c8d3dc;
  }
  * { margin: 0; padding: 0; box-sizing: border-box; }
  html, body { width: 1200px; height: 927px; overflow: hidden; background: var(--white); }
  body { font-family: "Source Sans 3", Arial, sans-serif; color: var(--ink); }
  .flyer { position: relative; width: 1200px; height: 927px; overflow: hidden; }
  .shapes { position: absolute; inset: 0; }

  .brand { position: absolute; left: 36px; top: 30px; display: flex; align-items: center; gap: 14px; }
  .brand-mark { width: 44px; height: 44px; background: var(--red); }
  .brand-name { font-size: 38px; font-weight: 400; color: var(--ink); letter-spacing: 0.5px; }

  .join-badge {
    position: absolute; left: 418px; top: 112px; width: 170px;
    transform: rotate(45deg); transform-origin: center;
    color: var(--white); font-weight: 700; text-align: center;
    font-size: 21px; line-height: 1.05; letter-spacing: 2px;
  }

  .photo {
    position: absolute; left: 585px; top: 12px; width: 210px; height: 233px;
    background: linear-gradient(180deg, #b9c7d3 0%, #dfe5ea 60%, #f2f2f2 100%);
  }

  .headline {
    position: absolute; left: 0; top: 255px; width: 1200px; text-align: center;
    color: var(--red); font-weight: 700; font-size: 18px; letter-spacing: 1.6px;
  }

  .about {
    position: absolute; left: 40px; top: 296px; width: 510px;
    font-size: 14px; line-height: 1.32; letter-spacing: 1px; color: var(--body-grey);
  }
  .about h3 { font-size: 13.5px; font-weight: 400; text-align: right; letter-spacing: 1px; margin: 0 0 10px; }
  .about h3 strong { font-weight: 700; }
  .about .list { text-align: right; margin-bottom: 18px; }
  .about .centered { text-align: center; margin-bottom: 18px; }
  .about .justified { text-align: justify; margin-bottom: 18px; }
  .about .justified-right { text-align: justify; text-align-last: right; }

  .connect {
    position: absolute; left: 610px; top: 288px; width: 518px; color: var(--white);
    font-size: 15px; line-height: 1.32; letter-spacing: 1.4px;
  }
  .connect h2 { font-size: 25px; font-weight: 400; letter-spacing: 1.5px; margin-bottom: 6px; }
  .connect h2 strong, .connect h4 strong { font-weight: 700; }
  .connect p { text-align: justify; }
  .connect h4 { font-size: 19px; font-weight: 400; letter-spacing: 0.5px; margin: 22px 0 8px; }
  .connect ul { list-style: none; font-style: italic; margin-bottom: 26px; }
  .connect li { position: relative; padding-left: 30px; margin-bottom: 2px; }
  .connect li::before { content: ""; position: absolute; left: 2px; top: 7px; width: 7px; height: 7px; border-radius: 50%; background: var(--white); }

  .footer-strip { position: absolute; left: 255px; top: 862px; display: flex; align-items: center; gap: 12px; }
  .partner-name { display: flex; align-items: center; gap: 6px; font-size: 14px; color: var(--ink); }
  .partner-name .dot { width: 16px; height: 16px; background: var(--red); }
  .partner-badge { width: 56px; height: 44px; background: #e3e3e3; border-radius: 50%; }
  .partner-badge.square { border-radius: 4px; width: 80px; height: 34px; background: #c9d8ea; }
  .sponsor-label { font-size: 13px; letter-spacing: 1px; color: var(--ink); margin-left: 10px; }
  .sponsor-name { font-size: 22px; color: #7a1f5c; font-weight: 600; }
</style>
</head>
<body>
<main class="flyer">
  <svg class="shapes" width="1200" height="927" viewBox="0 0 1200 927" aria-hidden="true">
    <polygon points="740,0 800,0 800,245 720,245" fill="#e3e8ec"/>
    <polygon points="795,50 890,50 800,140" fill="#e3e8ec"/>
    <polygon points="345,100 425,28 505,100 565,100 565,245 420,245 420,175" fill="var(--red)"/>
    <polygon points="40,283 572,283 572,795 545,817 40,817" fill="var(--grey-panel)"/>
    <polygon points="585,283 1140,283 1140,545 1200,600 1200,790 1140,860 1140,927 585,927" fill="var(--dark-panel)"/>
  </svg>

  <div class="brand">
    <span class="brand-mark"></span>
    <span class="brand-name">MX Bridge</span>
  </div>

  <div class="join-badge">JOIN<br>mxbridge.org<br>TODAY!</div>

  <div class="photo" role="img" aria-label="Photograph of three smiling women in white tops against a pale sky"></div>

  <h1 class="headline">YOUR INFORMATION WILL LEAD TO FUTURE TREATMENTS AND CURES FOR ALL TYPES OF LIPODYSTROPHY</h1>

  <section class="about">
    <h3>WHO CAN <strong>PARTICIPATE</strong></h3>
    <p class="list">Patients<br>Family members<br>Healthcare providers<br>Investigators &amp; researchers<br>All stakeholders interested in RTQV</p>

    <h3>HOW IT <strong>WORKS</strong></h3>
    <p class="centered">Patients can join the registry to submit their data.<br>After taking web-based surveys, explore the collected information in a way that protects the privacy of everyone.</p>

    <h3>WHO <strong>WE ARE</strong></h3>
    <p class="justified">As its name implies, MX Bridge represents the coming together of a wide range of entities and individuals who recognize the value in pooling their combined expertise and information. The Governing Board of MX Bridge comes from leaders in the non-profit sector, government agencies and academic institutions.</p>
    <p class="justified-right">Regardless of their individual backgrounds, the thought leaders of MX Bridge share a common goal to increase the community’s ability to help one another through improved communication, and by doing so, to help the millions of people affected by Lipodystrophy.</p>
  </section>

  <section class="connect">
    <h2>GET <strong>CONNECTED.</strong></h2>
    <p>One of the most important steps towards finding effective treatments for lipodystrophy (LD) is to uncover the ways in which the diseases behave, the symptoms that are commonly seen and how those symptoms progress. This requires the collection of as much information as possible about all people affected by LD. MX Bridge will serve as that database–the critical link between the patient community and the scientific community. The more people who join the registry the greater the chances that research will produce results that benefit everyone.</p>
    <h4>Join <strong>THE BRIDGE RTQV</strong> Registry to:</h4>
    <ul>
      <li>Tell us about your experience with LD and learn about the experiences with others</li>
      <li>Share information in a program that protects your privacy</li>
      <li>Provide valuable quality-of-life information that can be used to advocate on behalf of the LD community</li>
      <li>Help the research community launch clinical trials and studies</li>
    </ul>
    <p>We need to hear YOUR VOICE and we hope you will decide to join MX Bridge. Every individual who joins makes a vital contribution toward helping all of those affected by lipodystrophy.</p>
  </section>

  <div class="footer-strip">
    <span class="partner-name"><span class="dot"></span>Patient Unity Group</span>
    <span class="partner-badge"></span>
    <span class="partner-badge"></span>
    <span class="partner-badge square"></span>
    <span class="sponsor-label">Sponsored by:</span>
    <span class="sponsor-name">Northvale Pharma</span>
  </div>
</main>
</body>
</html>
```